KVR Biz Cards

We are a property management company that manages luxury level residential estates. As such, we need a business card design that gives a high end feel. The idea at the moment is to list the services offered on the back of the card, and our company information on the front of the card.

Services for the back of the card are as follows:
Professional Property Management service, Home Hosting & Concierge Service, Holliday Home / Income Property Management

```html
<!DOCTYPE html>
<html lang="en">
<head>
<meta charset="utf-8">
<title>KVR Biz Cards</title>
<link href="https://fonts.googleapis.com/css2?family=Montserrat:wght@500;600&family=Roboto:wght@400;500;700&display=swap" rel="stylesheet">
<style>
  :root {
    --backdrop: #5f3d1d;
    --card: #f3f2f2;
    --ink: #1f1c1c;
    --panel: #1c1a1a;
    --bronze: #9a6a3a;
    --white: #ffffff;
  }
  * { box-sizing: border-box; margin: 0; padding: 0; }
  html, body {
    width: 1200px; height: 900px; overflow: hidden;
    background: var(--backdrop);
    font-family: "Roboto", Arial, sans-serif;
    color: var(--ink);
  }
  .canvas { position: relative; width: 1200px; height: 900px; }
  .card {
    position: absolute; left: 337px; width: 525px; height: 300px;
    background: var(--card);
    overflow: hidden;
  }
  .card--front { top: 130px; }
  .card--back { top: 470px; }

  /* Front */
  .brand-panel {
    position: absolute; left: 18px; top: 18px; width: 225px; height: 264px;
    background: var(--panel);
    display: flex; flex-direction: column; align-items: center; justify-content: center;
    text-align: center;
  }
  .brand-mark {
    display: flex; align-items: center; gap: 8px;
    font-family: "Montserrat", Arial, sans-serif; font-weight: 600;
    font-size: 34px; letter-spacing: 1px; color: var(--bronze);
    line-height: 1; margin-bottom: 10px;
  }
  .brand-mark__square { width: 14px; height: 14px; background: var(--bronze); }
  .brand-name {
    font-family: "Montserrat", Arial, sans-serif; font-weight: 600;
    font-size: 11.5px; letter-spacing: 0.3px; color: var(--white);
    white-space: nowrap;
  }
  .brand-tagline {
    font-family: "Montserrat", Arial, sans-serif; font-weight: 500;
    font-size: 7.6px; letter-spacing: 0.3px; color: var(--bronze);
    margin-top: 2px; white-space: nowrap;
  }
  .identity { position: absolute; left: 272px; top: 68px; }
  .identity__name {
    font-weight: 700; font-size: 21px; color: var(--bronze); letter-spacing: 0.2px; line-height: 1.1;
  }
  .identity__title { font-size: 16px; color: var(--ink); margin-top: 4px; line-height: 1.1; }
  .contacts { position: absolute; left: 272px; top: 155px; list-style: none; }
  .contact { display: flex; align-items: flex-start; gap: 15px; margin-bottom: 11px; }
  .contact__icon {
    width: 23px; height: 23px; background: var(--bronze); flex: none;
    display: flex; align-items: center; justify-content: center;
  }
  .contact__text { font-size: 14.5px; line-height: 17.5px; padding-top: 2px; color: var(--ink); }

  /* Back */
  .back-brand {
    position: absolute; top: 34px; left: 0; right: 0;
    display: flex; flex-direction: column; align-items: center; text-align: center;
  }
  .back-brand .brand-name { color: var(--ink); font-size: 12.5px; }
  .back-brand .brand-tagline { font-size: 8.2px; }
  .services-band {
    position: absolute; left: 0; right: 0; top: 142px; height: 35px;
    background: var(--bronze);
    display: flex; align-items: center; justify-content: center;
    font-weight: 700; font-size: 20px; color: var(--white); letter-spacing: 0.3px;
  }
  .services {
    position: absolute; left: 0; right: 0; top: 195px; height: 82px;
    display: grid; grid-template-columns: 1fr 1fr 1fr; list-style: none;
  }
  .service {
    display: flex; flex-direction: column; align-items: center; text-align: center;
    font-size: 12px; line-height: 15px; color: var(--ink);
  }
  .service + .service { border-left: 1.5px solid var(--bronze); }
  .service__icon { width: 40px; height: 36px; margin-bottom: 12px; }
</style>
</head>
<body>
<main class="canvas">

  <section class="card card--front" aria-label="Business card front">
    <div class="brand-panel">
      <div class="brand-mark"><span class="brand-mark__square"></span>KVR</div>
      <p class="brand-name">KESTREL VALE RESIDENCES</p>
      <p class="brand-tagline">Quiet Care for Every Fine Residence</p>
    </div>

    <div class="identity">
      <p class="identity__name">YOUR NAME</p>
      <p class="identity__title">TITLE</p>
    </div>

    <ul class="contacts">
      <li class="contact">
        <span class="contact__icon">
          <svg width="13" height="13" viewBox="0 0 24 24"><path fill="#fff" d="M6.6 10.8a15.2 15.2 0 0 0 6.6 6.6l2.2-2.2c.3-.3.7-.4 1-.2 1.1.4 2.3.6 3.6.6.6 0 1 .4 1 1V20c0 .6-.4 1-1 1A17 17 0 0 1 3 4c0-.6.4-1 1-1h3.5c.6 0 1 .4 1 1 0 1.3.2 2.5.6 3.6.1.3 0 .7-.2 1z"/></svg>
        </span>
        <span class="contact__text">012-555-0148</span>
      </li>
      <li class="contact">
        <span class="contact__icon">
          <svg width="13" height="11" viewBox="0 0 24 20"><rect x="2" y="2" width="20" height="16" rx="1.5" fill="none" stroke="#fff" stroke-width="2"/><path d="M3 4l9 7 9-7" fill="none" stroke="#fff" stroke-width="2"/></svg>
        </span>
        <span class="contact__text">hello@kestrelvale.com</span>
      </li>
      <li class="contact">
        <span class="contact__icon">
          <svg width="11" height="14" viewBox="0 0 20 26"><path fill="#fff" d="M10 0a10 10 0 0 0-10 10c0 7 10 16 10 16s10-9 10-16A10 10 0 0 0 10 0zm0 14a4 4 0 1 1 0-8 4 4 0 0 1 0 8z"/></svg>
        </span>
        <span class="contact__text">214 Elm Crest Road,<br>Northvale 40922</span>
      </li>
    </ul>
  </section>

  <section class="card card--back" aria-label="Business card back">
    <div class="back-brand">
      <div class="brand-mark"><span class="brand-mark__square"></span>KVR</div>
      <p class="brand-name">KESTREL VALE RESIDENCES</p>
      <p class="brand-tagline">Quiet Care for Every Fine Residence</p>
    </div>

    <div class="services-band">SERVICES</div>

    <ul class="services">
      <li class="service">
        <svg class="service__icon" viewBox="0 0 40 36">
          <path d="M10 17L22 6l12 11M13 15v8h18v-8" fill="none" stroke="var(--bronze)" stroke-width="2.4" stroke-linejoin="round"/>
          <rect x="20" y="13" width="4" height="4" fill="var(--bronze)"/>
          <path d="M2 24c6-1 10 2 16 2h10l8-4c2-1 3 1 1 2l-10 7c-3 2-6 2-9 1L4 30z" fill="var(--bronze)"/>
        </svg>
        <span>Professional Property<br>Management service</span>
      </li>
      <li class="service">
        <svg class="service__icon" viewBox="0 0 40 36">
          <path d="M5 16L20 3l15 13M9 13v20h22V13" fill="none" stroke="var(--bronze)" stroke-width="2.4" stroke-linejoin="round"/>
          <path d="M13 26a7 7 0 0 1 14 0z" fill="var(--bronze)"/>
          <rect x="11" y="27" width="18" height="2" fill="var(--bronze)"/>
          <circle cx="20" cy="17.5" r="1.5" fill="var(--bronze)"/>
        </svg>
        <span>Home Hosting &amp;<br>Concierge Service</span>
      </li>
      <li class="service">
        <svg class="service__icon" viewBox="0 0 40 36">
          <path d="M5 16L20 3l15 13M9 13v20h22V13" fill="none" stroke="var(--bronze)" stroke-width="2.4" stroke-linejoin="round"/>
          <text x="20" y="25" text-anchor="middle" font-family="Roboto, Arial, sans-serif" font-weight="700" font-size="11" fill="var(--bronze)">$</text>
        </svg>
        <span>Holliday Home / Income<br>Property Management</span>
      </li>
    </ul>
  </section>

</main>
</body>
</html>
```